Visitenkarten-Design für Psychiaterin
Zielgruppe
Dr. med. Helene Marbach, Ärztin, Psychotherapie für Kinder Jugendliche und Erwachsene, spezialisiert auf komplexe Posttraumatische Belastungsstörung, Dissoziative Störungen, Persönlichkeitsstörungen, Bindungsstörungen, LUMO-Mentorin
Das Design soll modern sein, Seriosität Professionalität, Dynamik und Geborgenheit ausstrahlen. Zielgruppe sind Menschen die traumatische Situationen überlebt haben.
Aufgabenstellung
Name, Fachgebiet und Spezialisierung, Telefonnummer, e-Mail
Unter Dateiupload sind Visitenkartenbeispiele die mir gefallen

```html
<!DOCTYPE html>
<html lang="de">
<head>
<meta charset="utf-8">
<title>Visitenkarte – Dr. med. Helene Marbach</title>
<link rel="stylesheet" href="https://fonts.googleapis.com/css2?family=Fira+Sans+Condensed:wght@400;600;700&display=swap">
<style>
  :root {
    --stage: #bcb8b0;
    --paper: #f5f5f3;
    --slate: #575755;
    --accent: #82bc1f;
    --ink: #545452;
    --light-ink: #ffffff;
  }
  * { box-sizing: border-box; margin: 0; padding: 0; }
  html, body {
    width: 1200px; height: 807px; overflow: hidden;
    background: var(--stage);
    font-family: "Fira Sans Condensed", "Arial Narrow", sans-serif;
  }
  .stage {
    position: relative; width: 1200px; height: 807px;
    display: flex; justify-content: center; align-items: center; gap: 40px;
  }
  .card {
    position: relative; width: 540px; height: 349px;
    background: var(--paper);
    box-shadow: 0 6px 18px rgba(0,0,0,0.18);
    overflow: hidden;
  }
  .card__band {
    position: absolute; left: 0; right: 0; top: 182px; bottom: 0;
    background: var(--slate);
    border-top: 6px solid var(--accent);
  }
  .marker {
    display: inline-block; width: 17px; height: 17px;
    background: var(--accent); flex: none;
  }
  .marker--small { width: 11px; height: 11px; margin: 0 8px; }
  .name {
    display: flex; align-items: center; gap: 12px;
    font-weight: 700; color: var(--ink); letter-spacing: -0.2px; white-space: nowrap;
  }

  /* Rückseite mit Details */
  .card--details .name { position: absolute; left: 26px; top: 22px; font-size: 30px; }
  .specialisation {
    position: absolute; left: 26px; right: 26px; top: 66px;
    font-size: 19.5px; line-height: 1.12; color: var(--ink);
  }
  .contact {
    position: absolute; right: 26px; bottom: 22px; left: 26px;
    color: var(--light-ink); font-size: 21px; line-height: 1.3; text-align: right;
  }
  .contact__line { display: flex; justify-content: flex-end; align-items: center; white-space: nowrap; }
  .contact__line--phone { padding-right: 0; }
  .contact__line--address { padding-right: 12px; }
  .contact__line--web { padding-right: 28px; }

  /* Vorderseite */
  .card--front .name {
    position: absolute; right: 26px; top: 120px; font-size: 37px;
  }
  .role {
    position: absolute; right: 30px; top: 228px;
    color: var(--light-ink); font-size: 22px; line-height: 1.25; text-align: center;
  }
</style>
</head>
<body>
<main class="stage">
  <article class="card card--details">
    <div class="card__band"></div>
    <h2 class="name"><span class="marker"></span>Dr. med. Helene Marbach</h2>
    <p class="specialisation">spezialisiert auf komplexe Posttraumatische Belastungsstörung, Dissoziative Störungen, Persönlichkeitsstörungen, Bindungsstörungen, LUMO-Mentorin</p>
    <div class="contact">
      <p class="contact__line contact__line--phone">Tel. 04712-358190</p>
      <p class="contact__line contact__line--address">Lindenweg 7<span class="marker marker--small"></span>34567 Auenfeld</p>
      <p class="contact__line contact__line--web">www.praxis-marbach.de<span class="marker marker--small"></span>kontakt@praxis-marbach.de</p>
    </div>
  </article>

  <article class="card card--front">
    <div class="card__band"></div>
    <h1 class="name"><span class="marker"></span>Dr. med. Helene Marbach</h1>
    <p class="role">Ärztin, Psychotherapie für Kinder,<br>Jugendliche und Erwachsene</p>
  </article>
</main>
</body>
</html>
```